Kindled Harvest Christian Ministry needs a Conference Ad

We are a Christian nonprofit focused on eliminating systemic poverty and helping believers function as ministers in their workplaces. The 2025 Kindled Harvest Global Conference coming up in October, and we need an ad for social media (facebook, instagram, and X) and our website in order to get people excited to attend! We are looking for a modern and sleek design that incorporates our logo (attached file). You can either put just the butterfly and then write our company name separately somewhere in the design or use it as is (we used Gotham font for the logo). We want to emphasize the joy of in-person connection at the conference, so you could possibly include stock photos of young people gathering together. You could also include the attached photo of our founders in the design and say “with Len and Marta Drubeck". Also, include the conference dates, which are October 9-12, 2025, and say “come in person or join online”. Lastly, please include the tagline “from the Coastal Awakening to Worldwide Transformation”. NOTE: I’m attaching AN EXAMPLE I’ve created of how the design could look, which you can feel free to use for inspiration.
Target Market(s)
Young people on Instagram and facebook
Font styles to use
Other font styles liked:
- Gotham
Look and feel

```html
<!DOCTYPE html>
<html lang="en">
<head>
<meta charset="utf-8">
<title>Kindled Harvest Global Conference 2025</title>
<link rel="stylesheet" href="https://fonts.googleapis.com/css2?family=Montserrat:wght@300;400;600;700;800&display=swap">
<style>
  :root {
    --navy: #2b2d55;
    --white: #ffffff;
    --sky-top: #c9c3a8;
    --sky-bottom: #8f7a5e;
    --city-dark: #3b3a3c;
    --crowd-dark: #1f2a28;
    --crowd-warm: #5a4a3e;
    --glow: rgba(28, 24, 10, 0.95);
  }
  * { margin: 0; padding: 0; box-sizing: border-box; }
  html, body { width: 1200px; height: 1200px; overflow: hidden; background: var(--navy); }
  body { font-family: "Montserrat", Arial, sans-serif; color: var(--white); }

  .ad { position: relative; width: 1200px; height: 1200px; overflow: hidden; background: var(--navy); }

  .skyline-photo {
    position: absolute; left: 0; top: 0; width: 1200px; height: 336px;
    background: linear-gradient(180deg, var(--sky-top) 0%, #b3a486 45%, var(--sky-bottom) 70%, var(--city-dark) 100%);
  }
  .headline {
    position: absolute; left: 0; top: 92px; width: 1200px;
    text-align: center; font-weight: 800; font-size: 61px; line-height: 96px;
    letter-spacing: 1px; text-transform: uppercase;
    text-shadow: 0 0 10px var(--glow), 0 0 18px var(--glow), 0 0 4px var(--glow);
  }

  .info-band { position: absolute; left: 0; top: 336px; width: 1200px; height: 522px; background: var(--navy); }

  .rule { position: absolute; left: 108px; width: 625px; height: 4px; background: var(--white); }
  .rule--top { top: 415px; }
  .rule--bottom { top: 598px; }

  .attend {
    position: absolute; left: 108px; top: 438px; width: 625px;
    text-align: center; font-weight: 400; font-size: 61px; line-height: 70px;
    letter-spacing: 1px; text-transform: uppercase;
  }
  .dates {
    position: absolute; left: 108px; top: 630px; width: 625px;
    text-align: center; font-weight: 700; font-size: 50px; line-height: 62px;
  }
  .hosts {
    position: absolute; left: 108px; top: 729px; width: 659px; height: 62px;
    background: var(--white); color: var(--navy);
    font-weight: 700; font-size: 33px; line-height: 62px; padding-left: 44px;
  }

  .brand {
    position: absolute; left: 833px; top: 455px; width: 280px;
    display: flex; align-items: center; gap: 16px;
    font-weight: 700; font-size: 34px; line-height: 40px; color: var(--white);
  }
  .brand-mark { width: 26px; height: 26px; flex: none; background: var(--white); }

  .crowd-photo {
    position: absolute; left: 0; top: 858px; width: 1200px; height: 342px;
    background: linear-gradient(160deg, var(--crowd-warm) 0%, #3a3832 45%, var(--crowd-dark) 100%);
  }
  .tagline {
    position: absolute; left: 131px; top: 908px; width: 620px;
    font-weight: 400; font-size: 44px; line-height: 70px; letter-spacing: 1px;
    text-shadow: 0 0 10px var(--glow), 0 0 16px var(--glow);
  }

  .founders-frame {
    position: absolute; left: 778px; top: 628px; width: 383px; height: 400px;
    background: var(--white); padding: 26px 28px 28px 28px;
  }
  .founders-photo {
    width: 100%; height: 100%;
    background: radial-gradient(ellipse at 55% 55%, #c79b78 0%, #7a5a48 40%, #2a2220 100%);
  }
</style>
</head>
<body>
<main class="ad">
  <div class="skyline-photo" role="img" aria-label="Photo of a downtown city skyline at sunset"></div>
  <h1 class="headline">Kindled Harvest<br>Global Conference 2025</h1>

  <section class="info-band"></section>
  <div class="rule rule--top"></div>
  <p class="attend">Come in person<br>or join online</p>
  <div class="rule rule--bottom"></div>
  <p class="dates">October 9-12, 2025</p>
  <p class="hosts">with Len and Marta Drubeck</p>

  <div class="brand">
    <span class="brand-mark"></span>
    <span>Kindled Harvest</span>
  </div>

  <div class="crowd-photo" role="img" aria-label="Photo of young people gathered together in worship with raised hands"></div>
  <p class="tagline">From the Coastal Awakening to Worldwide Transformation</p>

  <div class="founders-frame">
    <div class="founders-photo" role="img" aria-label="Portrait photo of founders Len and Marta Drubeck smiling together"></div>
  </div>
</main>
</body>
</html>
```